Kelro DIGITAL HORIZON learning portal

We beed a flyer design to launch our new DIGITAL HORIZON Learning Portal. The flyer will be used in letter box drops and to give to small business to encourage sales of this new service.

ABOUT US:

We are a small training firm offering world class training solutions in the areas of:

1. Time Management
2. Sales skills
3. Strategic & High performance leadership
4. Sales Management
5. Personal Maximum Achievement.

You can find our website at www.kelro-example.com.au

ABOUT DIGITAL HORIZON Learning Portal:

We are launching an online learning portal called DIGITAL HORIZON Learning Portal which will allow anyone, anywhere in the world to take our courses online as long as they have access to a PC, smart phone and internet.

Taking an online course with Kelro through our DIGITAL HORIZON Learning Portal will allow students/participants to save over 50% of the normal price of attending a face to face training program.

There are over 80 different individual learning units that can be taken by a student/participant. The participant can choose to take any unit they wish building their own unique learning experience or they can take a full course in one of the subject areas listed above in the about us section.

ADVANTAGES OF USING THE Kelro DIGITAL HORIZON Learning Portal:

* Cost effective, save over 50% by learning online compared to attending a Kelro class room based programme.
* learning can be scheduled around work and family
* Reduces travel time and travel costs
* Students/participants have the option to select learning materials that meets their level of knowledge and interest.
* Complete flexibility to build a personalised learning experience.
* Students/participants can study anywhere they have access to a computer and Internet connection
* Self-paced learning modules allow students/participants to work at their own pace
* Develops knowledge of the Internet and computers skills that will help learners throughout their lives and careers
* Successfully completing online or computer-based courses builds self-knowledge and self-confidence and encourages students to take responsibility for their learning
* Join over 4 million people who have successfully undertaken the training world wide at a time & a place convenient to students/participants.
* pay securely using swiftcoin
* learn based on a students/participants personal financial circumstances with individual units priced at $82.50 each (this is Australian dollars & includes GST)

The final design will be one that conveys flexibility of learning, cost effectiveness of the online learning solution. The flyer design can either be folded, single or double sided, A4 or A5 or DL size - whatever works best in the final outcome.

Industry/Entity Type

Small Business

Requirements
Must have
• The flyer must include:

* the "DIGITAL HORIZON Learning portal" logo and the "Kelro logo" and use the Kelro font. Several logos have been provided and the most appropriate ones can be chosen for the design. The font has been provided. (I do have other logo files in different file formats if required to aid designers)

* The flyer must direct people to the Kelro website www.kelro-example.com.au to pay, enrol and find out other information about the courses.

* The flyer must highlight cost effectiveness of the solution, the world wide popularity of the programs (over 4 million people have completed the programs world wide), flexibility of learning & the diversity of study areas.

Because of price changes in future of courses it would be very beneficial to be able to edit files in future to show new prices if and when that happens.

```html
<!DOCTYPE html>
<html lang="en">
<head>
<meta charset="utf-8">
<title>Kelro – DIGITAL HORIZON Learning Portal flyer</title>
<link rel="stylesheet" href="https://fonts.googleapis.com/css2?family=Roboto+Condensed:wght@300;400;700&family=Roboto:wght@400;700&display=swap">
<style>
  :root {
    --stage: #e4e6e9;
    --paper: #ffffff;
    --blue: #1a86c4;
    --blue-deep: #0b4f86;
    --blue-light: #5fb3e6;
    --navy: #0a2e57;
    --grey-box: #e5e6e8;
    --grey-bar: #9da3aa;
    --text: #4a4f55;
    --photo-a: #d9dde2;
    --photo-b: #f3f4f6;
  }
  * { box-sizing: border-box; margin: 0; padding: 0; }
  html, body { width: 1200px; height: 750px; overflow: hidden; }
  body { background: var(--stage); position: relative; font-family: "Roboto", Arial, sans-serif; }

  .flyer {
    position: absolute; top: 35px; width: 480px; height: 680px;
    background: var(--paper); overflow: hidden;
    box-shadow: 0 6px 18px rgba(0,0,0,.18);
  }
  .flyer--front { left: 100px; }
  .flyer--back  { left: 620px; }

  /* brand name (logo stand-in) */
  .brand { display: flex; align-items: center; gap: 8px; }
  .brand__square { width: 22px; height: 22px; background: var(--blue); }
  .brand__name {
    font-family: "Roboto Condensed", Arial, sans-serif; font-weight: 700;
    font-size: 26px; color: var(--blue-deep); letter-spacing: .5px;
  }

  /* front */
  .front__photo {
    position: absolute; left: 0; top: 0; width: 480px; height: 360px;
    background: linear-gradient(135deg, var(--photo-b), var(--photo-a));
  }
  .front__panel { position: absolute; left: 0; top: 0; }
  .front__title {
    position: absolute; left: 150px; top: 300px; width: 340px;
    transform: rotate(23.6deg); transform-origin: left top;
    font-family: "Roboto Condensed", Arial, sans-serif; text-align: right;
    line-height: 1;
  }
  .front__title-main { display: block; font-weight: 700; font-size: 34px; color: var(--navy); }
  .front__title-sub  { display: block; font-weight: 300; font-size: 34px; color: #fff; margin-top: 4px; }

  /* back */
  .back__brand { position: absolute; right: 28px; top: 28px; }
  .back__photo {
    position: absolute; left: 0; top: 88px; width: 480px; height: 190px;
    background: linear-gradient(135deg, var(--photo-b), var(--photo-a));
  }
  .advantages {
    position: absolute; left: 0; top: 278px; width: 480px; height: 282px;
    background: var(--grey-box); padding: 18px 34px 0 34px;
  }
  .advantages__heading {
    font-family: "Roboto Condensed", Arial, sans-serif; font-weight: 700;
    font-size: 17px; line-height: 1.15; color: var(--text);
    border-bottom: 2px solid var(--grey-bar); padding-bottom: 8px; margin-bottom: 10px;
    position: relative;
  }
  .advantages__heading em { font-style: normal; color: var(--blue); }
  .advantages__heading::after {
    content: ""; position: absolute; right: -34px; bottom: -2px;
    width: 18px; height: 30px; background: var(--blue);
  }
  .advantages__list { list-style: none; font-size: 12px; line-height: 1.35; color: var(--text); }
  .advantages__list li { position: relative; padding-left: 14px; margin-bottom: 2px; }
  .advantages__list li::before {
    content: ""; position: absolute; left: 0; top: 5px; width: 5px; height: 5px; background: var(--blue);
  }
  .url-bar {
    position: absolute; left: 0; top: 560px; width: 400px; height: 38px;
    background: var(--blue); color: #fff; padding-left: 34px;
    font-family: "Roboto Condensed", Arial, sans-serif; font-weight: 700; font-size: 20px;
    line-height: 38px; letter-spacing: .5px;
  }
  .url-bar__tail {
    position: absolute; right: 0; top: 572px; width: 70px; height: 14px; background: var(--blue);
  }
  .back__footer-brand { position: absolute; left: 0; right: 0; top: 612px; display: flex; justify-content: center; }
  .contact {
    position: absolute; left: 0; right: 0; bottom: 14px; text-align: center;
    font-size: 10.5px; color: var(--text);
  }
  .contact a { color: var(--blue); text-decoration: none; }
</style>
</head>
<body>

<section class="flyer flyer--front">
  <div class="front__photo" role="img" aria-label="Photo of a business team working at laptops around a meeting table"></div>
  <svg class="front__panel" width="480" height="680" viewBox="0 0 480 680" aria-hidden="true">
    <defs>
      <radialGradient id="panel-glow" cx="0.3" cy="0.45" r="0.9">
        <stop offset="0" stop-color="var(--blue-light)"/>
        <stop offset="0.5" stop-color="var(--blue)"/>
        <stop offset="1" stop-color="var(--blue-deep)"/>
      </radialGradient>
    </defs>
    <polygon points="0,170 480,380 480,680 0,680" fill="url(#panel-glow)"/>
  </svg>
  <h1 class="front__title">
    <span class="front__title-main">DIGITAL HORIZON</span>
    <span class="front__title-sub">LEARNING PORTAL</span>
  </h1>
</section>

<section class="flyer flyer--back">
  <div class="brand back__brand">
    <span class="brand__square"></span><span class="brand__name">Kelro</span>
  </div>
  <div class="back__photo" role="img" aria-label="Photo of three smiling business people standing together"></div>

  <div class="advantages">
    <h2 class="advantages__heading"><em>ADVANTAGES</em> of using the Kelro<br>DIGITAL HORIZON Learning Portal:</h2>
    <ul class="advantages__list">
      <li>Cost effective</li>
      <li>Time flexibility</li>
      <li>Reduces travel time and travel costs</li>
      <li>Option to select learning materials that meets their level of knowledge and interest.</li>
      <li>Complete flexibility to build a personalised learning experience.</li>
      <li>Study anywhere – when access to a computer and Internet connection</li>
      <li>Self-paced learning modules</li>
      <li>Pay securely using swiftcoin</li>
      <li>Learn based on a personal financial circumstances with individual units priced at $82.50 each (this is Australian dollars &amp; includes GST)</li>
    </ul>
  </div>

  <div class="url-bar">WWW.KELRO-EXAMPLE.COM.AU</div>
  <div class="url-bar__tail"></div>

  <div class="back__footer-brand">
    <div class="brand"><span class="brand__square"></span><span class="brand__name">Kelro</span></div>
  </div>
  <p class="contact">14 Harlow Street Newtown, NSW 2042<br>Phone: <a href="tel:+61255501234">+61 2 5550 1234</a> | Website: <a href="https://www.kelro-example.com.au">www.kelro-example.com.au</a></p>
</section>

</body>
</html>
```